Tuning Company need an advertising banner for fileservice b2b (chiptuning) in vector

Hello everyone,
we need an advertising banner for fileservice b2b (chip tuning).
Plinkora, other social networks and outdoor as advertising.
I use the WINols program, and many nice pictures on google for background or other things ,.
I want a professional design. complete new design. (not my example here at my designs)
maybe you have a slogan too?
Text:
TUNING FILE SERVICE FOR PROFESSIONALS
🔥 File service 🔥 by German ENGINEERING since 2012!
Test my service now‼ ️
Conditions:
✅ECO, Stage 1 + 2 € 100
DRW TQ4 / TR7 / KARVO3-5-7-9 / DORALU ✅ECO, Stage 1 + 2 150 €
KVT / ZUPO RHX42 / TQ4 / TR7 / LUNQ38 / PAK52
✅ECO, Stage 1 + 2 150 €
Vext Harluff QBT864
✅ECO, Stage 1 + 2 150 €
Valtorin TQ4 / TR7
✅ECO, Stage 1 + 2 150 €
TRUCK / HGV / TRACTOR
✅ECO, Stage 1 + 2 150 €
More service:
Stage 3 and more available
EGR, DPF and more .... ✅ + 50 €
✔️NOXELA / SCR OFF
✔️KVT SPORTS DISPLAY
✔️BSC (Boost Sensor Calibration)
✔️COLD START NOISE
✔️DPF / FAP OFF
✔️KLX TUNE ✅ + € 100
✔️DTC OFF
✔️EGR OFF
✔️EVAP REMOVAL
✔️EXHAUST FLAP REMOVAL
✔️GPF / OPF OFF ✅ + € 100
✔️HARDCUT POPCORN LIMITER (DIESEL ONLY)
✔️HOT START
✔️IMMO OFF
✔️MAF OFF
✔️O2 / LAMBA OFF
✔️ORIGINAL FILE REQUEST
✔️POP & BANG
✔️READINESS CALIBRATION
✔️SAP DELETE (Secondry Air Pump)
✔️SPEED LIMIT OFF
✔️START STOP DISABLE
✔️SWIRL FLAPS
✔️TQ MONITORING OFF
✔️TVA OFF
☑️German ZEB and invoice no problem❗
Attention‼ my working time:
Monday 09:00 - 21:00
Tuesday. 09:00 - 21:00
Wednesday. 09:00 - 21:00
Thursday. 09:00 - 21:00
Friday. 09:00 - 17:00
Saturday. 09:00 - 16:00
Sunday. Closed
Text end
-------------------------------------------------- --------------------------------------------
What is fileservice?
Explanation of chip tuning files and file service
Competent software development for chiptuner B2B (business-to-business) is our specialty. Our RAM-Pilo team has specialized in programming the original software for almost all engine control units. In addition to cars, we also supply commercial vehicles, tractors, motorcycles and boats with the necessary tuning software (chip tuning files).
In recent years, chip tuning has become more and more popular. The reasons for this are, in particular, the power advantages as well as the fuel savings and environmental compatibility. In this area, chip tuning is an accommodating alternative to the factory-programmed control unit. Chiptuning / software optimization is implemented by RAM-Pilo dealers depending on the vehicle using soldering, BDM, BOOT, OBD or serial programming. With us, each tuning file (chip tuning file) is always produced individually for the respective customer vehicle and customer request.
Individual chip tuning files for dealers and chip tuners
Our services include software programming and file service for almost all cars and trucks. Motorcycles and Agriculture Makes. We offer this programming (chip tuning files, chip tuning files) to various dealers worldwide. With its chiptuning file service, RAMPILO supports more than 400 chiptuning companies, small and large chiptuners, as well as car workshops, truck dealers or agricultural companies with everything you need for professional chiptuning. We supply the best hardware for chip tuning, high quality software (chip tuning files and chip tuning files) and of course know-how! We also offer various training courses. If you have any questions, our engineers and employees are always available for you by email, WhatsApp and Skype.
You can reach us from 9 am to 8 pm seven days a week.
There are many file service suppliers for chiptuning files (chiptuning files)
The market is teeming with hobby tuners and chip tuning file suppliers who are able to manipulate tuning files more badly than right without being really aware of the effects of their actions. The consequences of inferior chip tuning files and poor file service support are gearbox damage, turbo damage, engine damage and bad experiences.
The programming of chip tuning files is a very complex topic that requires not only know-how but also daily expansion and updating of knowledge. We are constantly in close contact with well-known partners from the automotive industry. Only thanks to the certainty that we are always up to date, we can adapt our developments flexibly and promptly to the circumstances.

```html
<!DOCTYPE html>
<html lang="en">
<head>
<meta charset="utf-8">
<title>Veltrak – Tuning File Service</title>
<link href="https://fonts.googleapis.com/css2?family=Orbitron:wght@900&family=Roboto+Condensed:ital,wght@0,400;0,700;1,700&display=swap" rel="stylesheet">
<style>
  :root{
    --page:#dcdcdc;
    --paper:#ffffff;
    --ink:#262626;
    --dark:#2a2a2a;
    --gold:#d9a53c;
    --gold-light:#f1cf7a;
    --gold-deep:#b98a2c;
    --text:#2b2b2b;
    --white:#ffffff;
  }
  *{box-sizing:border-box;margin:0;padding:0}
  html,body{width:1200px;height:860px;overflow:hidden;background:var(--page)}
  body{font-family:"Roboto Condensed",Arial,sans-serif;color:var(--text);position:relative}
  .flyer{position:absolute;left:0;top:55px;width:1200px;height:750px;background:var(--paper);overflow:hidden}
  .shapes{position:absolute;inset:0}
  .brand{position:absolute;left:18px;top:28px;display:flex;align-items:center;gap:12px}
  .brand-mark{width:34px;height:34px;background:var(--gold)}
  .brand-name{font-family:"Roboto Condensed",Arial,sans-serif;font-weight:700;font-size:46px;color:var(--gold);letter-spacing:2px;line-height:1}
  .headline{position:absolute;left:0;top:94px;width:900px;height:127px}
  .tagline{position:absolute;left:17px;top:226px;font-weight:700;font-style:italic;font-size:31px;color:var(--ink);letter-spacing:.2px;line-height:1}
  .tag{position:absolute;display:flex;height:45px;filter:drop-shadow(1px 2px 2px rgba(0,0,0,.3))}
  .tag-price{background:linear-gradient(180deg,var(--gold-light),var(--gold) 55%,var(--gold-deep));
    clip-path:polygon(0 0,88% 0,100% 50%,88% 100%,0 100%);
    color:var(--ink);font-size:37px;line-height:45px;padding-left:5px;letter-spacing:-1px}
  .tag-info{margin-left:4px;background:var(--dark);color:var(--white);
    clip-path:polygon(0 0,93% 0,100% 50%,93% 100%,0 100%);
    font-size:11.5px;line-height:12.5px;padding:4px 14px 0 4px;display:flex;flex-direction:column;justify-content:center}
  .divider{position:absolute;left:18px;top:393px;width:521px;border-top:2px dotted #555}
  .section-tag{position:absolute;left:18px;top:408px;width:139px;height:28px;background:var(--dark);color:var(--white);
    clip-path:polygon(0 0,94% 0,100% 50%,94% 100%,0 100%);font-weight:700;font-size:15.5px;line-height:28px;padding-left:10px}
  .section-note{position:absolute;left:18px;top:440px;font-size:13.5px}
  .extras{position:absolute;left:0;top:0;width:800px;height:750px}
  .price-big{position:absolute;font-size:52px;line-height:1;color:var(--ink);letter-spacing:-2px}
  .checklist{position:absolute;list-style:none;font-size:10.5px;line-height:13px;text-transform:uppercase;color:var(--text)}
  .checklist li{position:relative;padding-left:13px}
  .checklist li svg{position:absolute;left:0;top:2px;width:9px;height:9px}
  .checklist .note{text-transform:none}
  .rule{position:absolute;left:293px;top:483px;height:128px;border-left:1px solid #333}
  .hours-title{position:absolute;left:22px;top:660px;font-weight:700;font-size:31px;color:var(--white);line-height:1}
  .hours-title .accent{color:var(--gold)}
  .hours{position:absolute;top:699px;height:27px;border:1px solid var(--gold);border-radius:2px;color:var(--white);
    font-size:15.5px;line-height:25px;text-align:center}
</style>
</head>
<body>
<svg width="0" height="0" style="position:absolute">
  <defs>
    <symbol id="tick" viewBox="0 0 10 10">
      <circle cx="5" cy="5" r="4.2" fill="none" stroke="#333" stroke-width="1"/>
      <path d="M3 5.2 L4.5 6.6 L7.2 3.6" fill="none" stroke="#333" stroke-width="1.1"/>
    </symbol>
  </defs>
</svg>

<main class="flyer">
  <svg class="shapes" viewBox="0 0 1200 750" width="1200" height="750">
    <defs>
      <linearGradient id="goldPhoto" x1="0" y1="0" x2="0" y2="1">
        <stop offset="0" stop-color="#e0b44c"/>
        <stop offset=".5" stop-color="#b8913e"/>
        <stop offset="1" stop-color="#6f5a34"/>
      </linearGradient>
      <linearGradient id="bluePhoto" x1="0" y1="0" x2="0" y2="1">
        <stop offset="0" stop-color="#cfe3e6"/>
        <stop offset=".35" stop-color="#8fb1a7"/>
        <stop offset=".5" stop-color="#1f2f8f"/>
        <stop offset=".8" stop-color="#1a2570"/>
        <stop offset="1" stop-color="#6c7276"/>
      </linearGradient>
    </defs>
    <rect class="footer-band" x="0" y="642" width="1200" height="108" fill="var(--dark)"/>
    <polygon role="img" aria-label="Gold-toned photo of a race car on a track" points="824,0 1043,0 849,318 984,700 827,700 664,278" fill="url(#goldPhoto)"/>
    <polygon points="1038,0 1200,0 1200,750 1003,750 846,318" fill="var(--dark)"/>
    <polygon role="img" aria-label="Photo of a blue sports car on a race circuit" points="1057,0 1200,0 1200,750 1018,750 862,318" fill="url(#bluePhoto)"/>
    <polygon class="headline-band" points="0,94 907,94 836,221 0,221" fill="var(--dark)"/>
  </svg>

  <div class="brand">
    <span class="brand-mark"></span>
    <span class="brand-name">VELTRAK</span>
  </div>

  <svg class="headline" viewBox="0 0 900 127" width="900" height="127">
    <defs>
      <linearGradient id="goldText" x1="0" y1="0" x2="0" y2="1">
        <stop offset="0" stop-color="#f6d886"/>
        <stop offset=".55" stop-color="#d9a53c"/>
        <stop offset="1" stop-color="#c0902f"/>
      </linearGradient>
    </defs>
    <text x="17" y="59" font-family="Orbitron, sans-serif" font-weight="900" font-size="56" fill="url(#goldText)" textLength="800" lengthAdjust="spacingAndGlyphs">TUNING FILE SERVICE</text>
    <text x="17" y="116" font-family="Orbitron, sans-serif" font-weight="900" font-size="56" fill="url(#goldText)" textLength="817" lengthAdjust="spacingAndGlyphs">FOR PROFESSIONALS</text>
  </svg>

  <p class="tagline">FILE SERVICE BY GERMAN ENGINEERING SINCE 2012!</p>

  <div class="tag" style="left:18px;top:280px">
    <div class="tag-price" style="width:75px">€100</div>
    <div class="tag-info" style="width:150px"><span>ECO, Stage 1 + 2</span><span>DRW TQ4 / TR7 /</span><span>KARVO3-5-7-9 / DORALU</span></div>
  </div>
  <div class="tag" style="left:241px;top:280px">
    <div class="tag-price" style="width:80px">€150</div>
    <div class="tag-info" style="width:155px"><span>ECO, Stage 1 + 2</span><span>KVT / ZUPO RHX42 / TQ4 /</span><span>TR7 / LUNQ38 / PAK52</span></div>
  </div>
  <div class="tag" style="left:478px;top:280px">
    <div class="tag-price" style="width:78px">€150</div>
    <div class="tag-info" style="width:155px"><span>ECO, Stage 1 + 2</span><span>TRUCK / HGV / TRACTOR</span></div>
  </div>
  <div class="tag" style="left:18px;top:335px">
    <div class="tag-price" style="width:75px">€150</div>
    <div class="tag-info" style="width:150px"><span>ECO, Stage 1 + 2</span><span>Vext Harluff QBT864</span></div>
  </div>
  <div class="tag" style="left:236px;top:335px">
    <div class="tag-price" style="width:78px">€150</div>
    <div class="tag-info" style="width:157px"><span>ECO, Stage 1 + 2</span><span>Valtorin TQ4 / TR7</span></div>
  </div>

  <div class="divider"></div>
  <div class="section-tag">MORE SERVICES</div>
  <p class="section-note">Stage 3 and more available EGR, DPF and more ....</p>

  <svg class="extras" viewBox="0 0 800 750" width="800" height="750">
    <polygon points="18,465 698,465 778,629 18,629" fill="none" stroke="#444" stroke-width="1" stroke-dasharray="3 2"/>
  </svg>

  <div class="price-big" style="left:24px;top:525px">€50</div>
  <ul class="checklist" style="left:126px;top:521px;line-height:13.6px">
    <li><svg><use href="#tick"/></svg>NOXELA / SCR OFF</li>
    <li><svg><use href="#tick"/></svg>KVT SPORTS DISPLAY</li>
    <li><svg><use href="#tick"/></svg><span class="note">BSC (Boost Sensor Calibration)</span></li>
    <li><svg><use href="#tick"/></svg>COLD START NOISE</li>
    <li><svg><use href="#tick"/></svg>DPF / FAP OFF</li>
  </ul>

  <div class="rule"></div>

  <div class="price-big" style="left:304px;top:525px">€100</div>
  <ul class="checklist" style="left:413px;top:470px">
    <li><svg><use href="#tick"/></svg>KLX TUNE</li>
    <li><svg><use href="#tick"/></svg>DTC OFF</li>
    <li><svg><use href="#tick"/></svg>EGR OFF</li>
    <li><svg><use href="#tick"/></svg>EVAP REMOVAL</li>
    <li><svg><use href="#tick"/></svg>EXHAUST FLAP REMOVAL</li>
    <li><svg><use href="#tick"/></svg>GPF / OPF OFF</li>
    <li><svg><use href="#tick"/></svg>HARDCUT POPCORN LIMITER<br>(DIESEL ONLY)</li>
    <li><svg><use href="#tick"/></svg>HOT START</li>
    <li><svg><use href="#tick"/></svg>IMMO OFF</li>
    <li><svg><use href="#tick"/></svg>MAF OFF</li>
    <li><svg><use href="#tick"/></svg>O2 / LAMBA OFF</li>
  </ul>
  <ul class="checklist" style="left:571px;top:472px">
    <li><svg><use href="#tick"/></svg>ORIGINAL FILE REQUEST</li>
    <li><svg><use href="#tick"/></svg>POP &amp; BANG</li>
    <li><svg><use href="#tick"/></svg>READINESS CALIBRATION</li>
    <li><svg><use href="#tick"/></svg>SAP DELETE<br><span class="note">(Secondry Air Pump)</span></li>
    <li><svg><use href="#tick"/></svg>SPEED LIMIT OFF</li>
    <li><svg><use href="#tick"/></svg>START STOP DISABLE</li>
    <li><svg><use href="#tick"/></svg>SWIRL FLAPS</li>
    <li><svg><use href="#tick"/></svg>TQ MONITORING OFF</li>
    <li><svg><use href="#tick"/></svg>TVA OFF</li>
  </ul>

  <h2 class="hours-title"><span class="accent">ATTENTION!!</span> MY WORKING TIME:</h2>
  <div class="hours" style="left:22px;width:237px">MONDAY - THRSDAY&nbsp; 09:00 - 21:00</div>
  <div class="hours" style="left:265px;width:155px">FRIDAY. 09:00 - 17:00</div>
  <div class="hours" style="left:428px;width:175px">SATURDAY. 09:00 - 16:00</div>
  <div class="hours" style="left:612px;width:125px">SUNDAY CLOSED</div>
</main>
</body>
</html>
```